Income Tax Business Cards - Updates

Need to update these business cards while keeping all the same wording but just update them and make them look nicer and more modern/ on brand with our brand.

Industry/Entity Type

finance

Contact Information for Business Card

we have multiple locations so will just need to easily be able to change the address and phone numbers

Colors

Designer to choose colors to be used in the design.

```html
<!DOCTYPE html>
<html lang="en">
<head>
<meta charset="UTF-8">
<title>Income Tax Business Cards</title>
<link href="https://fonts.googleapis.com/css2?family=Montserrat:wght@400;500;600;700;800;900&display=swap" rel="stylesheet">
<style>
  :root {
    --backdrop: #e5e5e7;
    --paper: #f1f1f0;
    --green: #2e6347;
    --red: #dc3240;
    --ink: #333335;
    --muted: #4a4a4c;
  }
  * { margin: 0; padding: 0; box-sizing: border-box; }
  html, body {
    width: 1200px; height: 1200px; overflow: hidden;
    background: var(--backdrop);
    font-family: "Montserrat", sans-serif;
  }
  .card {
    position: absolute;
    left: 289px;
    width: 622px;
    height: 355px;
    background: var(--paper);
    overflow: hidden;
  }
  .card--front { top: 212px; }
  .card--back { top: 632px; }
  .line {
    position: absolute; left: 0; right: 0;
    display: flex; justify-content: center; align-items: center;
    white-space: nowrap; line-height: 1;
  }

  /* front */
  .front-tab {
    position: absolute; left: 112px; width: 399px; top: 0; height: 54px;
    background: var(--green);
    border-radius: 0 0 20px 20px;
  }
  .front-headline {
    top: 78px; height: 38px;
    color: var(--red); font-weight: 600; font-size: 45px; letter-spacing: 0.4px;
  }
  .front-band {
    position: absolute; left: 0; right: 0; top: 148px; bottom: 0;
    background: var(--green);
  }
  .front-amount {
    top: 188px; height: 60px;
    color: var(--red); font-weight: 900; font-size: 77px;
    -webkit-text-stroke: 2px #f4f4f4; paint-order: stroke fill;
  }
  .front-advance {
    top: 278px; height: 42px;
    color: #f2f2f2; font-weight: 600; font-size: 51px; letter-spacing: 0.5px;
  }

  /* back */
  .contact { position: absolute; left: 35px; top: 12px; }
  .contact-phone { color: var(--red); font-weight: 600; font-size: 29px; line-height: 1; }
  .contact-address {
    margin-top: 14px; list-style: none;
    color: var(--muted); font-weight: 400; font-size: 19px; line-height: 23px;
  }
  .brand {
    position: absolute; left: 352px; top: 38px;
    display: flex; align-items: center; gap: 8px;
    color: var(--green); font-weight: 700; font-size: 22px; line-height: 26px;
  }
  .brand-dot { flex: none; width: 14px; height: 14px; border-radius: 50%; background: var(--red); }
  .brand-name { text-align: center; }
  .growth-bars { position: absolute; left: 502px; top: 97px; }
  .estimates-band {
    top: 137px; height: 51px; background: var(--green);
    color: #f2f2f2; font-weight: 800; font-size: 36px; letter-spacing: 9px;
    padding-left: 9px;
  }
  .back-amount {
    top: 199px; height: 52px;
    color: var(--red); font-weight: 900; font-size: 62px;
  }
  .back-advance {
    top: 264px; height: 38px;
    color: var(--ink); font-weight: 700; font-size: 42px; letter-spacing: 5px;
    padding-left: 5px;
  }
  .returns-tab {
    position: absolute; left: 116px; width: 390px; top: 309px; height: 46px;
    background: var(--green); border-radius: 20px 20px 0 0;
    display: flex; justify-content: center; align-items: center;
    color: #f2f2f2; font-weight: 600; font-size: 23px; white-space: nowrap;
  }
</style>
</head>
<body>
  <section class="card card--front">
    <div class="front-tab"></div>
    <h1 class="line front-headline">FILE YOUR TAXES HERE</h1>
    <div class="front-band"></div>
    <p class="line front-amount">UP TO $6,000</p>
    <p class="line front-advance">SAME DAY ADVANCE</p>
  </section>

  <section class="card card--back">
    <div class="contact">
      <p class="contact-phone">(555) 555 - 5555</p>
      <ul class="contact-address">
        <li>ADDRESS LINE - 1</li>
        <li>ADDRESS LINE - 2</li>
        <li>ADDRESS LINE - 3</li>
      </ul>
    </div>
    <div class="brand"><span class="brand-dot"></span><span class="brand-name">Ledger One<br>Financial</span></div>
    <svg class="growth-bars" width="88" height="41" viewBox="0 0 88 41" aria-hidden="true">
      <rect x="0" y="30" width="15" height="11" fill="var(--green)"/>
      <rect x="23" y="21" width="15" height="20" fill="var(--green)"/>
      <rect x="46" y="11" width="15" height="30" fill="var(--green)"/>
      <rect x="70" y="0" width="15" height="41" fill="var(--green)"/>
    </svg>
    <p class="line estimates-band">FREE ESTIMATES!</p>
    <p class="line back-amount">UP TO $6,000</p>
    <p class="line back-advance">SAME DAY ADVANCE</p>
    <p class="returns-tab">ON APPROVED TAX RETURNS!</p>
  </section>
</body>
</html>
```